Design Packaging for Monte Alba Coffee

Please look at website at www.montealbacoffeecompany.example
Need packaging for new coffee company. The size is: 6 x 9 x 3"

```html
<!DOCTYPE html>
<html lang="en">
<head>
<meta charset="utf-8">
<title>Monte Alba Coffee – Cacao Powder Packaging</title>
<link rel="stylesheet" href="https://fonts.googleapis.com/css2?family=Source+Sans+3:wght@300;400;700;800&display=swap">
<style>
  :root {
    --canvas: #efe9e5;
    --white: #ffffff;
    --ink: #2b2a33;
    --orange: #e5802a;
    --orange-deep: #d66f22;
    --yellow: #f2d46c;
    --pink: #ea8b84;
    --green: #5fc93c;
    --green-deep: #54bb33;
  }
  * { box-sizing: border-box; margin: 0; padding: 0; }
  html, body { width: 1200px; height: 720px; overflow: hidden; }
  body {
    background: var(--canvas);
    font-family: "Source Sans 3", sans-serif;
  }
  .lineup {
    position: relative;
    width: 1200px;
    height: 720px;
    display: flex;
    justify-content: center;
    align-items: center;
    gap: 45px;
  }
  .pouch {
    position: relative;
    width: 300px;
    height: 470px;
    border-radius: 8px 8px 14px 14px;
    overflow: hidden;
    color: var(--white);
  }
  .pouch--orange { background: var(--orange); }
  .pouch--pink { background: var(--pink); }
  .pouch--green { background: var(--green); }
  .pouch__art {
    position: absolute;
    inset: 0;
    width: 100%;
    height: 100%;
  }
  .pouch__zip {
    position: absolute;
    left: 0; right: 0;
    top: 44px;
    height: 4px;
    border-top: 1px solid rgba(0,0,0,.12);
    border-bottom: 1px solid rgba(255,255,255,.25);
  }
  .pouch__title {
    position: absolute;
    left: 0; right: 0;
    top: 100px;
    text-align: center;
    font-weight: 700;
    font-size: 62px;
    line-height: .92;
    letter-spacing: .5px;
  }
  .pouch__brand {
    position: absolute;
    left: 0; right: 0;
    top: 230px;
    text-align: center;
    font-weight: 300;
    font-size: 20px;
    letter-spacing: .3px;
  }
  .pouch__brand--upper { text-transform: uppercase; }
  .pouch__benefits {
    position: absolute;
    left: 0; right: 0;
    top: 270px;
    display: flex;
    justify-content: center;
    align-items: center;
    gap: 8px;
    font-size: 12px;
    font-weight: 400;
  }
  .pouch__benefits .dot {
    width: 7px; height: 7px;
    transform: rotate(45deg);
    background: currentColor;
  }
  .pouch--pink .pouch__benefits { color: var(--ink); gap: 18px; }
  .pouch--green .pouch__benefits { color: var(--ink); }
  .pouch--orange .pouch__benefits { color: rgba(255,255,255,.9); }
  .pouch__weight {
    position: absolute;
    font-size: 12px;
  }
  .pouch--orange .pouch__weight {
    left: 34px; top: 412px;
    width: 52px; text-align: center;
    font-weight: 700; font-size: 10px;
  }
  .pouch--pink .pouch__weight { left: 24px; top: 432px; color: var(--ink); }
  .pouch--green .pouch__weight { left: 24px; top: 420px; }
</style>
</head>
<body>
<main class="lineup">

  <article class="pouch pouch--orange">
    <svg class="pouch__art" viewBox="0 0 300 470" aria-hidden="false">
      <defs>
        <radialGradient id="podGlow" cx="50%" cy="50%" r="60%">
          <stop offset="0%" stop-color="#e2732b"/>
          <stop offset="55%" stop-color="#d94c3f"/>
          <stop offset="100%" stop-color="#6fae57"/>
        </radialGradient>
      </defs>
      <path d="M0 292 C80 272 200 262 300 282 L300 470 L0 470Z" fill="var(--yellow)"/>
      <g role="img" aria-label="Illustration of cacao pods with green leaves">
        <ellipse cx="170" cy="370" rx="105" ry="78" fill="url(#podGlow)" opacity=".85"/>
      </g>
      <circle cx="60" cy="418" r="27" fill="var(--orange-deep)"/>
    </svg>
    <div class="pouch__zip"></div>
    <h2 class="pouch__title">CACAO<br>POWDER</h2>
    <p class="pouch__brand pouch__brand--upper">Monte Alba Coffee</p>
    <ul class="pouch__benefits">
      <li style="list-style:none">Antioxidant</li><span class="dot"></span>
      <li style="list-style:none">Iron &amp; Magnesium</li><span class="dot"></span>
      <li style="list-style:none">Mood Booster</li>
    </ul>
    <p class="pouch__weight">Net 200g</p>
  </article>

  <article class="pouch pouch--pink">
    <svg class="pouch__art" viewBox="0 0 300 470">
      <defs>
        <linearGradient id="powderPhoto" x1="0" y1="0" x2="1" y2="0">
          <stop offset="0%" stop-color="#3e3e44"/>
          <stop offset="40%" stop-color="#6b5a52"/>
          <stop offset="100%" stop-color="#8b5a3f"/>
        </linearGradient>
      </defs>
      <g role="img" aria-label="Photo of cacao powder in a glass bowl">
        <path d="M15 330 C110 318 200 322 288 292 L288 428 C200 440 100 428 15 405Z" fill="url(#powderPhoto)"/>
      </g>
    </svg>
    <div class="pouch__zip"></div>
    <h2 class="pouch__title">CACAO<br>POWDER</h2>
    <p class="pouch__brand">Monte Alba coffee</p>
    <ul class="pouch__benefits">
      <li style="list-style:none">Antioxidant</li>
      <li style="list-style:none">Iron &amp; Magnesium</li>
      <li style="list-style:none">Mood Booster</li>
    </ul>
    <p class="pouch__weight">Net Wt 200g</p>
  </article>

  <article class="pouch pouch--green">
    <svg class="pouch__art" viewBox="0 0 300 470">
      <defs>
        <linearGradient id="podLines" x1="0" y1="0" x2="1" y2="1">
          <stop offset="0%" stop-color="#4fae30" stop-opacity=".5"/>
          <stop offset="100%" stop-color="#3f9a28" stop-opacity=".6"/>
        </linearGradient>
      </defs>
      <path d="M0 318 C100 300 200 332 300 298 L300 470 L0 470Z" fill="var(--green-deep)"/>
      <g role="img" aria-label="Line drawings of cacao pods">
        <rect x="20" y="340" width="260" height="70" rx="35" fill="url(#podLines)"/>
      </g>
    </svg>
    <div class="pouch__zip"></div>
    <h2 class="pouch__title">CACAO<br>POWDER</h2>
    <p class="pouch__brand pouch__brand--upper">Monte Alba Coffee</p>
    <ul class="pouch__benefits">
      <li style="list-style:none">Antioxidant</li><span class="dot"></span>
      <li style="list-style:none">Iron &amp; Magnesium</li><span class="dot"></span>
      <li style="list-style:none">Mood Booster</li>
    </ul>
    <p class="pouch__weight">Net Wt 200g</p>
  </article>

</main>
</body>
</html>
```